Property Developer - Simple yet Sophisticated and Sharp Business Card

We are a medium sized property developer involved mainly in townhouse developments and land subdivisions.

The company is looking for a simple, sharp and sophisticated business card that will be given to contractors, land owners, financiers etc and thus will need to look professional.

Property development related graphics and art can be used, however the card is not to be too "busy" or crowded. Our company name is KL Estates which could possibly be incorporated into the graphics or artwork.

Single sided and/or double sided designs will be acceptable.

A Simple, Sophisticated, Sharp design please!

Good Luck !

```html
<!DOCTYPE html>
<html lang="en">
<head>
<meta charset="utf-8">
<title>KL Estates – Business Card</title>
<link rel="stylesheet" href="https://fonts.googleapis.com/css2?family=Arimo:wght@400;700&display=swap">
<style>
  :root {
    --backdrop: #3b3b3d;
    --card-white: #ffffff;
    --brand-blue: #1ba3db;
    --band-deep: #1679a6;
    --band-mid: #2b9fd0;
    --band-light: #5cc0e6;
    --brand-grey: #6d6e70;
    --label-grey: #9a9a9a;
    --ink: #1c1c1c;
  }
  * { margin: 0; padding: 0; box-sizing: border-box; }
  html, body {
    width: 1200px; height: 900px; overflow: hidden;
    background: var(--backdrop);
    font-family: "Arimo", Arial, sans-serif;
  }
  .canvas { position: relative; width: 1200px; height: 900px; }

  .card {
    position: absolute;
    width: 660px; height: 360px;
    left: 208px;
    background: var(--card-white);
    border-radius: 22px;
    overflow: hidden;
  }
  .card--front { top: 62px; }
  .card--back { top: 472px; }

  .pattern-band {
    position: absolute; left: 0; width: 100%; height: 105px;
    background: linear-gradient(90deg, var(--band-deep) 0%, var(--band-mid) 30%, var(--band-light) 50%, var(--band-mid) 70%, var(--band-deep) 100%);
  }
  .pattern-band--top { top: 0; }
  .pattern-band--bottom { bottom: 0; }

  .brand {
    position: absolute; left: 0; width: 100%;
    display: flex; align-items: center; justify-content: center; gap: 12px;
  }
  .card--front .brand { top: 152px; }
  .card--back .brand { top: 86px; }
  .brand__mark {
    width: 26px; height: 26px; background: var(--brand-blue);
  }
  .brand__name {
    font-weight: 700; font-size: 40px; color: var(--brand-grey);
    letter-spacing: 0.5px;
  }

  .holder {
    position: absolute; left: 20px; top: 264px; width: 200px;
    text-align: center;
  }
  .holder__name {
    font-weight: 700; font-size: 27px; line-height: 32px; color: var(--brand-blue);
    white-space: nowrap;
  }
  .holder__title {
    font-weight: 700; font-size: 10px; color: var(--label-grey);
    letter-spacing: 0.8px; margin-top: 2px;
  }

  .divider {
    position: absolute; left: 229px; top: 232px;
    width: 5px; height: 100px;
    background: linear-gradient(180deg, var(--brand-blue), var(--band-deep));
  }

  .contact {
    position: absolute; left: 250px; top: 234px;
    list-style: none; font-size: 16px; line-height: 25px;
  }
  .contact__row { display: flex; }
  .contact__label {
    width: 62px; font-weight: 700; color: var(--label-grey);
  }
  .contact__value { color: var(--ink); }
</style>
</head>
<body>
<main class="canvas">
  <section class="card card--front" aria-label="Business card front">
    <div class="pattern-band pattern-band--top" role="img" aria-label="Blue band with a pattern of light rounded bricks"></div>
    <div class="brand">
      <span class="brand__mark"></span>
      <span class="brand__name">KL Estates</span>
    </div>
    <div class="pattern-band pattern-band--bottom" role="img" aria-label="Blue band with a pattern of light rounded bricks"></div>
  </section>

  <section class="card card--back" aria-label="Business card back">
    <div class="brand">
      <span class="brand__mark"></span>
      <span class="brand__name">KL Estates</span>
    </div>

    <div class="holder">
      <p class="holder__name">Dorian Vessick</p>
      <p class="holder__title">PRINCIPAL</p>
    </div>

    <div class="divider"></div>

    <ul class="contact">
      <li class="contact__row"><span class="contact__label">Phone:</span><span class="contact__value">(07) 3000 4821</span></li>
      <li class="contact__row"><span class="contact__label">Fax:</span><span class="contact__value">(07) 3000 4822</span></li>
      <li class="contact__row"><span class="contact__label">Email:</span><span class="contact__value">projects.klestates@mailbox.com</span></li>
      <li class="contact__row"><span class="contact__label">Postal:</span><span class="contact__value">PO Box 2150 Rivergate East QLD 4170</span></li>
    </ul>
  </section>
</main>
</body>
</html>
```